WE ARE REACHING OUT TO CONTRACTORS TO HAVE AN OPPORTUNITY TO PROVIDE PROPOSALS FOR THEIR PROJECTS.

WE ARE A WASHINGTON DC. METRO AREA PLUMBING, HEATING AND AIR CONDITIONING CONTRACTOR. WE WOULD LIKE TO PRESENT A POSTCARD THAT OFFERS A FRENDLY, CONVENIENT WAY TO PROVIDE PROPOSALS FOR THEIR UP COMMING PROJECTS. WE WOULD APPRECIATE THE OPPURTUNITY TO PROVIDE ESTIMATES FOR YOUR UP COMMING PROJECTS. IF REQUESTED, WE WILL PROVIDE SAME DAY WALK THRU'S AND PROPOSALS. GET A 2ND OPINION, WE ALL LOOK AT PROJECTS DIFFERENTLY. CUSTOM HOMES, SUB DIVISIONS, REMODELING, SEWER AND WATER INSTALLATIONS AND REPLACEMENTS, WELL AND SEPTIC INSTALLATIONS AND REPAIRS, MECHANICAL EQUIPTMENT CHANGE OUTS, PLUMBING SYSTEMS REPLACEMENTS AND REPAIRS. RESIDENTAL AND COMERICAL CONSTRUCTION.. " WE DO IT ALL" JUST GIVE US A CALL. " WE WILL BE THERE " I WOULD LIKE MY BUSINESS CARD ON THE FRONT WITH SOME MODIFICATIONS AND THE ABOVE DESCRIPTION ON THE BACK. " HIGHLIGHTING WE WOULD APPRICATE THE OPPORTUNITY TO WORK WITH YOU COMPANY " SAME DAY WALK THRU'S AND PROPOSALS. PLEASE ADDRESS THE TOP OF THE BACK IN BOLD PRINT. " ATTENTION ESTIMATING " EYE CATCHING COLORS PLEASE. THANK YOU, TODD WEMLEY

```html
<!DOCTYPE html>
<html lang="en">
<head>
<meta charset="utf-8">
<title>Wemley Mechanical Postcard</title>
<link rel="stylesheet" href="https://fonts.googleapis.com/css2?family=Michroma&family=Lato:wght@700;900&display=swap">
<style>
  :root {
    --red: #e3202a;
    --red-deep: #c8141d;
    --black: #0d0d0d;
    --white: #ffffff;
    --grey-light: #e6e6e6;
    --ink: #1a1a1a;
    --grey-text: #3a3a3a;
    --navy: #2c3d63;
  }
  * { margin: 0; padding: 0; box-sizing: border-box; }
  html, body { width: 1200px; height: 900px; overflow: hidden; background: var(--white); }
  .postcard { position: relative; width: 1200px; height: 900px; overflow: hidden;
    background: linear-gradient(180deg, var(--white) 0%, var(--grey-light) 100%); }
  .top-strip { position: absolute; left: 0; top: 0; width: 100%; height: 26px; background: var(--black); }
  .red-field { position: absolute; left: 0; top: 183px; width: 100%; height: 507px;
    background: radial-gradient(ellipse at 55% 55%, #f0323a 0%, var(--red) 45%, var(--red-deep) 100%); }
  .brand-box { position: absolute; left: 30px; top: 26px; width: 525px; height: 193px; background: var(--white);
    display: flex; align-items: center; padding-left: 40px; gap: 18px; }
  .brand-mark { width: 40px; height: 40px; background: var(--red); flex: none; }
  .brand-name { font-family: "Michroma", sans-serif; color: var(--ink); font-size: 27px; letter-spacing: 0.5px; }
  .headline { position: absolute; left: 32px; top: 268px; font-family: "Michroma", sans-serif;
    color: var(--white); font-size: 33px; line-height: 46px; letter-spacing: 1px; font-weight: 400;
    -webkit-text-stroke: 1.4px var(--white); }
  .worker-photo { position: absolute; left: 726px; top: 45px; width: 420px; height: 645px;
    border-radius: 190px 190px 0 0;
    background: linear-gradient(180deg, #3a4d78 0%, var(--navy) 50%, #1d2a47 100%); }
  .band { position: absolute; left: 0; top: 684px; width: 100%; height: 26px; background: var(--black); }
  .photo-frame { position: absolute; top: 584px; width: 237px; height: 165px; background: var(--black); padding: 8px; }
  .photo-frame .photo { width: 100%; height: 100%; }
  .frame-1 { left: 30px; } .frame-2 { left: 295px; } .frame-3 { left: 562px; }
  .photo-plumber { background: linear-gradient(135deg, #dfe6ee 0%, #4a6fa5 60%, #2e4a78 100%); }
  .photo-electric { background: linear-gradient(135deg, #c9ced4 0%, #8a8f96 50%, #2a2a2a 100%); }
  .photo-grinder { background: radial-gradient(circle at 70% 45%, #f3c25a 0%, #a8641f 35%, #2a1a10 100%); }
  .tagline { position: absolute; left: 0; top: 774px; width: 100%; text-align: center;
    font-family: "Michroma", sans-serif; font-size: 27px; letter-spacing: 0.5px; -webkit-text-stroke: 1.1px currentColor; }
  .tagline .accent { color: var(--red); }
  .tagline .dark { color: var(--ink); }
  .contact { position: absolute; left: 0; top: 814px; width: 100%; display: flex; justify-content: center;
    align-items: center; gap: 14px; font-family: "Lato", sans-serif; font-weight: 700; font-size: 31px; color: var(--grey-text); }
  .contact-item { display: flex; align-items: center; gap: 8px; }
  .contact svg { flex: none; }
  .bottom-strip { position: absolute; left: 0; bottom: 0; width: 100%; height: 28px; background: var(--red); }
</style>
</head>
<body>
<div class="postcard">
  <div class="top-strip"></div>
  <div class="red-field"></div>

  <div class="brand-box">
    <span class="brand-mark"></span>
    <span class="brand-name">Wemley Mechanical</span>
  </div>

  <h1 class="headline">36 YEARS RESIDENTIAL AND<br>COMMERCIAL REMODELING<br>PLUMBNG, HEATING, AIR<br>CONDITIONING,<br>GAS FITTING</h1>

  <div class="worker-photo" role="img" aria-label="Smiling tradesman in navy cap and coveralls holding a red pipe wrench, arms crossed"></div>

  <div class="band"></div>
  <div class="photo-frame frame-1"><div class="photo photo-plumber" role="img" aria-label="Plumber repairing pipes under a sink"></div></div>
  <div class="photo-frame frame-2"><div class="photo photo-electric" role="img" aria-label="Technician in hard hat working on an air conditioning unit's wiring"></div></div>
  <div class="photo-frame frame-3"><div class="photo photo-grinder" role="img" aria-label="Worker cutting metal with a grinder, sparks flying"></div></div>

  <p class="tagline"><span class="accent">WE DO IT ALL</span> <span class="dark">JUST GIVE US A CALL.</span><span class="accent">WE WILL BE THERE</span></p>

  <div class="contact">
    <span class="contact-item">
      <svg width="24" height="24" viewBox="0 0 24 24" aria-hidden="true">
        <rect x="1" y="1" width="22" height="22" rx="4" fill="#1a1a1a"/>
        <path d="M8 5.5c.6-.3 1.2 0 1.4.5l1 2.3c.2.5 0 1-.4 1.3l-.9.6c.6 1.5 1.6 2.7 3 3.5l.7-.8c.3-.4.9-.5 1.3-.3l2.2 1.1c.5.3.7.9.4 1.4l-.6 1.2c-.4.7-1.200 1.1-2 .9-3.9-1-6.8-4.2-7.5-8.1-.1-.8.3-1.6 1-2z" fill="#fff"/>
      </svg>
      301-555-0142
    </span>
    <span class="contact-item">
      <svg width="26" height="18" viewBox="0 0 26 18" aria-hidden="true">
        <rect x="0" y="0" width="26" height="18" fill="#1a1a1a"/>
        <path d="M1 1l12 9 12-9" fill="none" stroke="#fff" stroke-width="1.8"/>
      </svg>
      toddwemley@mailbox.com
    </span>
  </div>

  <div class="bottom-strip"></div>
</div>
</body>
</html>
```